Broschüren-Design für Wohnungsgesellschaft
Hallo Lorenz, die Zusammenarbeit hat richtig Spaß gemacht. Ich empfanf die gedankliche Herangehensweise als sehr professionell, die vielen Varianten waren eine Hilfe mich am Ende doch für meine Bauchentscheidung für die ersten Designvorschläge zu bestätigen. Sie sind ein toller Dienstleister, schnelle Reaktionen, Mitdenken, dabei immer freundlich, auch wenn ich das 4 mal mit dem gleichen Thema kam.
Zielgruppe
wir betreuen im Auftrag der Wohnungsgesellschaften Mieter die ihre Miete oder Mietnebenkosten nicht oder nur teilweise bezahlen.
Ziel ist,in einer telefonischen, email, Whatsapp-Betreuung, den Schuldnern einen Ausweg zu zeigen.
Wir nehmen den Schulder quasi an die Hand um in gemeinsamer Abstimmung d,h, Augenhöhe
Teilzahlungspläne zu erarbeiten und jeweils auch einzuhalten.
Ziel ist es die Würde des Schuldners zu bewahren und der Wohnungsgesellschaft die ihr zustehenden Summen zu sichern.
Das Ganze sehr im Unterschied zu brutalen und teueren Inkasso Aktivitäten einschlägiger Firmen.
Aufgabenstellung
lebendige, freundliche Darstellung, ohne dümmliche Gesichter telfonierender Damen,
plaktiv, doch klar1. die Zielgruppe der Broschüre sind Vorstände und GF größerer Wohnungsgesellschaften.
Diese Menschen haben ein Problem, dass nicht bezahlte Mieten, den Unternehmensertrag und die Liquidität der Gesellschaft negativ beeinflussen.
2. Si3e wollen natürlich die Mieten kassieren, gleichzeitig wollen Sie sich nicht als brutale Geldeintreiber in der Tageszeitung und in den Köpfen aller anderen Mieter wahrgenommen werden.
3. bislang gibt es in jeder Gesellschaft angestellte Mitarbeiter, die meist untrainiert die Beitreibung betreiben. Der Job ist selten gerne übernommen, die Tagesform bestimmt den Ton. Wenn der Mitarbeiter ausfällt ist meist kein Ersatz da.
4. in der Regel startet kurz nach dem Fälligkeitstermin ein automatisiertes schriftliches Mahnverfahren (per Computer) mit 1-3 Stufen, danach wandert das ganze zu professionellen Inkassounternehmen, die dicke Mahngebühren berechnen, den Schuldner bedrohen bis hin zu persönlichen Besuchen, der Gerichtsvollzieher ist dann die noch moderate Form.
5. der BTN Ansatz will genau das vermeiden, zumindest dort, wo ungeplante Umstände plötzliche Zahlungsengpässe verursachen oder Menschen nicht mit ihrem Geld richtig wirtschaften. Es geht nicht um die notorischen Zahlungsverweigerern.
Die Geschäftsführung der Gesellschaft soll und will das Gefühl haben, dass ihre Mieter auf Augenhöhe behandelt werden und genau deshalb kontinuierlich durch telefonische Ansprache, helfende Führung betreut werden, damit sie dartan arbeiten, die Mietshuld abzutragen und künftige Mieten pünktlich zahlen.
6. das wichtige Mittel ist der partnerschaftlich erstellte Zahlungsplan, der die Zahlungsmöglichkeiten in Raten des Mieters berücksichtig, der Grund ist, dass der Schuldner angesprochen werden kann, z.b. geht die Zahlung ein gelobt wird, kurz vorher an den Zahlungstermin erinn..

```html
<!DOCTYPE html>
<html lang="de">
<head>
<meta charset="utf-8">
<title>BTN Immobilienservices – Broschüre Mietschuldenmanagement</title>
<link rel="stylesheet" href="https://fonts.googleapis.com/css2?family=Figtree:wght@300;400;600;700;800&display=swap">
<style>
:root{
  --backdrop:#a9a9a9;
  --orange:#ef9420;
  --grey:#808080;
  --grey-dark:#5f5f5f;
  --white:#ffffff;
  --ink:#6b6b6b;
}
*{margin:0;padding:0;box-sizing:border-box}
html,body{width:1200px;height:2386px;overflow:hidden}
body{background:var(--backdrop);font-family:"Figtree",Arial,sans-serif;position:relative}
.abs{position:absolute}
.line{white-space:nowrap}
.text{z-index:2}

/* cover */
.cover{left:298px;top:238px;width:614px;height:442px}
.cover-photo{left:0;top:0;width:339px;height:442px;background:linear-gradient(160deg,#f7f7f7,#e2e2e2)}
.brand{left:30px;top:48px;display:flex;align-items:center;gap:8px;color:var(--grey-dark);font-size:13px;font-weight:600;white-space:nowrap}
.brand-square{width:12px;height:12px;background:var(--orange)}
.cover-panel{left:339px;top:0;width:275px;height:442px;background:var(--orange);color:var(--white)}
.cover-headline{right:27px;top:110px;text-align:right;font-size:19px;font-weight:700;line-height:25px;white-space:nowrap}
.tag{color:var(--white);font-weight:800;line-height:1;white-space:nowrap}
.cover-tag{left:87px;top:193px;width:188px;height:42px;background:var(--grey);font-size:40px;padding:1px 0 0 13px}
.cover-lead{right:27px;top:253px;text-align:right;font-size:17px;font-weight:300;line-height:21px;white-space:nowrap}
.cover-url{left:0;width:275px;top:415px;text-align:center;font-size:9px}

/* spread two */
.spread{width:818px}
.spread-two{left:182px;top:1047px;height:294px}
.page-left{left:0;top:0;width:405px;height:100%;background:linear-gradient(90deg,#f2f2f2,#e6e6e6)}
.page-right{left:405px;top:0;width:413px;height:100%;background:linear-gradient(90deg,#e9e9e9,#f6f6f6 30%,#f4f4f4)}
.kicker{left:19px;top:56px;font-size:13px;font-weight:600;color:var(--ink)}
.tag-orange{background:var(--orange)}
.tag-grey{background:var(--grey)}
.tag-small{height:24px;font-size:20px;padding:2px 6px 0 19px}
.note{left:19px;font-size:9px;color:#8a8a8a;font-weight:400}
.claim{left:19px;top:224px;font-size:11px;font-weight:700;color:var(--orange);line-height:13.5px}
.piggy{left:265px;top:30px;width:150px;height:264px;background:radial-gradient(ellipse at 55% 65%,#e6b94a,#c8962a 40%,rgba(230,230,230,0) 70%)}
.puzzle{left:0;top:0;width:170px;height:294px;background:linear-gradient(90deg,#9a9a9a,#c9c9c9 60%,rgba(240,240,240,0))}
.intro{right:19px;top:76px;text-align:right;font-size:10px;font-weight:700;color:var(--ink);line-height:12.5px}
.tag-help{right:0;top:138px;height:23px;font-size:21px;padding:1px 19px 0 7px;background:var(--orange)}
.body-right{right:19px;top:170px;text-align:right;font-size:9px;color:#858585;line-height:11px}

/* spread three */
.spread-three{left:182px;top:1800px;height:292px}
.side-band{left:0;top:0;width:188px;height:292px;background:var(--grey)}
.bird{left:188px;top:0;width:217px;height:292px;background:radial-gradient(ellipse at 50% 45%,#b5a66a,#8e8f7a 35%,#f6f6f6 70%)}
.quote{left:0;top:38px;width:203px;height:60px;background:var(--orange);color:var(--white);font-size:20px;font-weight:700;line-height:26px;padding:4px 0 0 19px;white-space:nowrap}
.story{left:19px;top:120px;width:150px;font-size:8.6px;color:#eeeeee;line-height:11px}
.story-strong{left:19px;top:213px;font-size:10px;font-weight:700;color:var(--white);line-height:12.5px}
.back-cover{left:405px;top:0;width:413px;height:292px;background:linear-gradient(90deg,#2f2f2f,#484848 25%,#3c3c3c)}
</style>
</head>
<body>

<section class="abs cover">
  <div class="abs cover-photo" role="img" aria-label="Foto: Hand übergibt einen Schlüsselbund in eine offene Hand"></div>
  <div class="abs brand"><span class="brand-square"></span>BTN Immobilienservices</div>
  <div class="abs cover-panel">
    <p class="abs cover-headline">Mieter wollen ihre<br>Miete pünktlich zahlen</p>
    <div class="abs tag cover-tag">Stimmt!</div>
    <p class="abs cover-lead">Manchmal kommt es leider<br>anders Deshalb braucht es ein<br>Optimiertes<br>Mietschuldenmanagement</p>
    <p class="abs cover-url">www.btn-wohnservice.de</p>
  </div>
</section>

<section class="abs spread spread-two">
  <div class="abs page-left">
    <div class="abs piggy" role="img" aria-label="Goldenes Sparschwein zwischen fallenden Goldmünzen"></div>
    <p class="abs kicker line text">Manche brauchen eine führende Hand</p>
    <div class="abs tag tag-small tag-orange text" style="left:0;top:109px">Stimmt!</div>
    <p class="abs note line text" style="top:146px">Sonst hilft nur noch Inkasso, damit Sie Ihr Geld bekommen…</p>
    <div class="abs tag tag-small tag-grey text" style="left:0;top:161px">Stimmt nicht!</div>
    <p class="abs note line text" style="top:199px">Angst verursacht Flucht oder den Kopf in den Sand stecken</p>
    <p class="abs claim line text">Mietschuldenmanagement&nbsp;&nbsp; 2.0<br>holt Ihr Geld auf Augenhöhe<br>mit dem Schuldner</p>
  </div>
  <div class="abs page-right">
    <div class="abs puzzle" role="img" aria-label="Schwarz-weiß Foto: zwei Hände fügen Puzzleteile zusammen"></div>
    <p class="abs intro line text">Unverhofft kommt oft, nicht immer, doch<br>meistens dann mit voller Wucht. Routinen<br>werden Makulatur.&nbsp; Guter Wille allein genügt<br>nicht mehr, wenn nur noch</p>
    <div class="abs tag tag-help text">Konkrete Hilfe</div>
    <p class="abs body-right line text">Dafür sorgt, dass der Kopf oben bleibt.<br>Ein empathischer Gesprächspartner öffnet<br>den Blick auf das Machbare, zeigt Wege auf,<br>erschließt Zahlungsversprechen<br>und die Bereitschaft diese auch einzuhalten.</p>
  </div>
</section>

<section class="abs spread spread-three">
  <div class="abs side-band"></div>
  <div class="abs bird" role="img" aria-label="Foto: kleiner Vogel mit einem Wurm im Schnabel"></div>
  <div class="abs quote text">“Der frühe Vogel<br>pickt den Wurm“</div>
  <p class="abs story text">Es ist eine Binsenweisheit, dass Schuldner bei Geldeingang denjenigen Gläubiger zuerst befriedigen / ihre Verpflichtungen in Teilen abtragen, der zeitnah und emotional am nächsten ist.</p>
  <p class="abs story-strong line text">Ein noch so kleiner Schritt<br>Richtung Kontoausgleich<br>spornt an, verschafft Lob<br>und Anerkennung</p>
  <div class="abs back-cover"></div>
</section>

</body>
</html>
```